Wren Hollow Honey Label Design

I need to design a label for my honey

Wren Hollow Honey - 100% Raw Natural Australian Honey from Flowerdale Victoria

I like clean uncluttered designs - ideally with a hexagon background to tie into the hive - not garish or too brightly coloured, classic to the point of being understated.
Would like the label to be a wrap around for our 500G jars

Label size is

face - 4CM
Height 6.5CM
Wrap around dimension 16 CM (corners are rounded)

Would like to include the "produce of Australia Logo on the side - image here https://www.tradesignsregistry.example/files/originlabelsjpg

Possibly some text on one of the sides also along the lines of

Natures gold from the Shire of Murrindindi. Our bees live and work in the beautiful countryside of Flowerdale, Victoria. We are an independent 100% Australian owned honey producer. our honey is made as nature intended, nothing added, taken away or blended with it, just pure raw natural honey. for more information or enquiries please drop us a line at wrenhollowhoney@example-mail.net

Our hives are in the countryside in Flowerdale and there are lots of parrots, Lorikeets and Cockatoos - the king parrots are particularly prevalent and we would very much like them to feature in the logo and be prominent in the label design

if it helps or you are looking for images of bees - I am a photographer and have some images of bees - are than happy to provide these in whatever formate works - here are some of my images https://www.snapgallery.example/member/Dmoorelens

Target Market(s)

People looking to purchase pure Australian honey, unadulterated and guaranteed 100% natural

Logo Text

Wren Hollow Honey, ( natures gold from Flowerdale) optional

Font styles to use
Decorative

Colors

Designer to choose colors to be used in the design.

Requirements
Must have
• A wren Hollow image (male green and red)
• uncluttered and clean image
• connection to nature and natural products
• Australian owned and produced
• Natural product
• Independent, Victorian ethical honey producer
• must look and feel all local business
• Sorry should have stated that the jars are 500gms, they will contain 500 grams of Honey
• Please see guidance for honey labelling
• https://bellcreekapiary.example/honey-labelling/
• regarding the nutritional content, we will need to include this
• I would also like to have a small section "Packed __/__/__ Batch____" to allow me to then insert a date in order to track product
• Wren Hollow Honey
• 4183 Tarnwick-Elby Road. Flowerdale. Victoria. 3717
Nice to have
• Hexagon background design to tie it to the bees
• Calorific content of honey, this can be found on the web easy enough
• I like the idea/concept of a gauge on the side of one of the side panels that shows people how much honey they have left and of course when it gets down to the bottom of the label suggests they get some more before they run out
Should not have
• lots of clashing vibrant colours - need to be classically understated and clean
• Must not be corporate, big business

```html
<!DOCTYPE html>
<html lang="en">
<head>
<meta charset="utf-8">
<title>Wren Hollow Honey – Jar Label</title>
<link rel="stylesheet" href="https://fonts.googleapis.com/css2?family=Anton&family=Patrick+Hand&display=swap">
<style>
  :root {
    --page: #ffffff;
    --hex-top: #f2a07a;
    --hex-mid: #f6b25c;
    --hex-bottom: #f7a21c;
    --gold-rim: #e9c97a;
    --gold-deep: #b88a2e;
    --ribbon: #ffffff;
    --ribbon-end: #efefef;
    --ribbon-shade: #d9d9d9;
    --ink: #4a3512;
    --ink-soft: #5a3a0e;
    --crown: #9bbf3a;
    --parrot-green: #3f6b3a;
  }
  html, body {
    margin: 0;
    padding: 0;
    width: 1200px;
    height: 849px;
    overflow: hidden;
    background: var(--page);
  }
  .label {
    position: relative;
    width: 1200px;
    height: 849px;
  }
  .label-art {
    position: absolute;
    inset: 0;
  }
  .stop-top { stop-color: var(--hex-top); }
  .stop-mid { stop-color: var(--hex-mid); }
  .stop-bottom { stop-color: var(--hex-bottom); }
  .stop-ribbon { stop-color: var(--ribbon); }
  .stop-ribbon-end { stop-color: var(--ribbon-end); }
  .hex-frame { fill: var(--gold-rim); stroke: var(--gold-deep); stroke-width: 3; }
  .ribbon-fold { fill: var(--ribbon-shade); }
  .ribbon-band { stroke: var(--gold-rim); stroke-width: 3; }
  .crown-emblem { fill: var(--crown); }
  .parrot-illustration { fill: var(--parrot-green); }
  .brand-line {
    position: absolute;
    left: 0;
    width: 1200px;
    margin: 0;
    text-align: center;
    font-family: "Anton", sans-serif;
    font-weight: 400;
    color: var(--ink);
    letter-spacing: 2px;
    line-height: 1;
  }
  .brand-line--first { top: 228px; font-size: 104px; }
  .brand-line--second { top: 350px; font-size: 104px; }
  .brand-line--third { top: 478px; font-size: 112px; }
  .tagline {
    position: absolute;
    left: 0;
    width: 1200px;
    text-align: center;
    font-family: "Patrick Hand", cursive;
    color: var(--ink-soft);
    margin: 0;
  }
  .tagline--main { top: 620px; font-size: 30px; }
  .tagline--origin { top: 656px; font-size: 19px; }
  .net-weight {
    position: absolute;
    left: 0;
    width: 1200px;
    top: 708px;
    text-align: center;
    font-family: "Patrick Hand", cursive;
    font-size: 28px;
    color: var(--ink-soft);
    margin: 0;
  }
</style>
</head>
<body>
<main class="label">
  <svg class="label-art" width="1200" height="849" viewBox="0 0 1200 849" xmlns="http://www.w3.org/2000/svg">
    <defs>
      <linearGradient id="hexFill" x1="0" y1="0" x2="0" y2="1">
        <stop offset="0" class="stop-top"/>
        <stop offset="0.55" class="stop-mid"/>
        <stop offset="1" class="stop-bottom"/>
      </linearGradient>
      <linearGradient id="ribbonFill" x1="0" y1="0" x2="0" y2="1">
        <stop offset="0" class="stop-ribbon"/>
        <stop offset="1" class="stop-ribbon-end"/>
      </linearGradient>
    </defs>

    <!-- hexagon panel -->
    <polygon class="hex-frame" points="600,40 905,215 905,625 600,800 295,625 295,215"/>
    <polygon class="hex-panel" points="600,58 890,224 890,616 600,782 310,616 310,224" fill="url(#hexFill)"/>

    <!-- ribbon folds -->
    <polygon class="ribbon-fold" points="240,600 300,560 300,640"/>
    <polygon class="ribbon-fold" points="960,600 900,560 900,640"/>
    <!-- ribbon band -->
    <path class="ribbon-band" d="M250,520 Q600,460 950,520 L950,610 Q600,560 250,610 Z" fill="url(#ribbonFill)"/>

    <!-- crown emblem -->
    <rect class="crown-emblem" x="575" y="170" width="50" height="40" rx="4"
          role="img" aria-label="Small green crown emblem"/>

    <!-- bird illustrations -->
    <rect class="parrot-illustration" x="320" y="330" width="60" height="110" rx="18"
          role="img" aria-label="Red and green parrot perched, facing right"/>
    <rect class="parrot-illustration" x="820" y="330" width="60" height="110" rx="18"
          role="img" aria-label="Red and green parrot perched, facing left"/>
  </svg>

  <h1 class="brand-line brand-line--first">WREN</h1>
  <p class="brand-line brand-line--second">HOLLOW</p>
  <p class="brand-line brand-line--third">HONEY</p>

  <p class="tagline tagline--main">100% Raw Natural</p>
  <p class="tagline tagline--origin">Australian Honey from Flowerdale Victoria</p>
  <p class="net-weight">500g</p>
</main>
</body>
</html>
```